Business Card Design for Property Development Company Director

I am looking for a professional and unforgettable business card design for our Director of our Property Development Company.
Please see attached .pptx file to find out what information to include. You don't have to follow the exact format shown in the file - I am interested to see your creative flair using the information provided.

```html
<!DOCTYPE html>
<html lang="en">
<head>
<meta charset="utf-8">
<title>Corvane Property Group – Business Card</title>
<link rel="stylesheet" href="https://fonts.googleapis.com/css2?family=Poppins:wght@400;500;600;700&display=swap">
<style>
  :root {
    --bg: #e9eaec;
    --white: #ffffff;
    --brand-blue: #1f55b5;
    --deep-blue: #1c46a3;
    --panel-grey: #5e5e5e;
    --panel-grey-dark: #4f4f4f;
    --muted: #7a7a7a;
    --ink: #3f3f3f;
  }
  * { box-sizing: border-box; margin: 0; padding: 0; }
  html, body { width: 1200px; height: 1030px; overflow: hidden; }
  body {
    background: var(--bg);
    font-family: "Poppins", sans-serif;
    position: relative;
  }
  .card {
    position: absolute;
    width: 560px;
    height: 320px;
    overflow: hidden;
    box-shadow: 0 10px 24px rgba(0,0,0,.18);
  }
  /* ---------- Front ---------- */
  .card-front { left: 140px; top: 120px; background: var(--white); }
  .front-shape { position: absolute; inset: 0; }
  .brand-lockup {
    position: absolute; left: 18px; top: 34px;
    display: flex; align-items: center; gap: 8px;
  }
  .brand-mark { width: 30px; height: 30px; background: var(--brand-blue); }
  .brand-name {
    font-weight: 600; font-size: 15px; line-height: 1.05;
    color: var(--brand-blue); letter-spacing: .5px; text-transform: uppercase;
  }
  .licence {
    position: absolute; left: 18px; top: 83px;
    font-size: 8px; color: var(--muted);
  }
  .skyline-art {
    position: absolute; right: 0; bottom: 0; width: 190px; height: 90px;
    background: linear-gradient(180deg, rgba(255,255,255,0) 0%, rgba(255,255,255,.07) 100%);
  }
  .contact-block { position: absolute; left: 279px; top: 66px; color: var(--white); }
  .person-name { font-weight: 700; font-size: 24px; letter-spacing: .3px; line-height: 1.1; }
  .person-role { font-size: 14px; font-weight: 400; margin-top: 2px; }
  .contact-list { list-style: none; margin-top: 22px; }
  .contact-list li {
    display: flex; align-items: center; gap: 8px;
    font-size: 17px; line-height: 1; height: 33px;
  }
  .contact-icon { width: 20px; height: 20px; flex: none; }

  /* ---------- Back ---------- */
  .card-back {
    left: 500px; top: 590px;
    background: linear-gradient(135deg, #2458bd 0%, var(--deep-blue) 100%);
    color: var(--white); text-align: center;
  }
  .house-art {
    position: absolute; left: 60px; right: 60px; top: 100px; bottom: 0;
    background: radial-gradient(ellipse at 50% 60%, rgba(255,255,255,.16) 0%, rgba(255,255,255,.06) 55%, rgba(255,255,255,0) 80%);
  }
  .tagline {
    position: relative; margin-top: 24px;
    font-weight: 600; font-size: 24px; line-height: 1.4; letter-spacing: .3px;
  }
  .back-lockup {
    position: relative; margin-top: 34px;
    display: flex; align-items: center; justify-content: center; gap: 14px;
  }
  .back-lockup .brand-mark { width: 58px; height: 58px; background: var(--white); }
  .back-lockup .brand-name {
    color: var(--white); font-size: 27px; font-weight: 600; text-align: left; letter-spacing: 1px;
  }
  .invite {
    position: absolute; left: 0; right: 0; bottom: 30px;
    font-size: 13px; font-weight: 400;
  }
</style>
</head>
<body>

<section class="card card-front">
  <svg class="front-shape" viewBox="0 0 560 320" aria-hidden="true">
    <defs>
      <linearGradient id="panelGrey" x1="0" y1="0" x2="0" y2="1">
        <stop offset="0" stop-color="#636363"/>
        <stop offset="1" stop-color="#555555"/>
      </linearGradient>
    </defs>
    <path d="M285 0 H560 V320 H272 C252 230 252 90 285 0 Z" fill="url(#panelGrey)"/>
    <path d="M275 0 H285 C252 90 252 230 272 320 H262 C240 230 240 90 275 0 Z" fill="#1f55b5"/>
  </svg>

  <div class="brand-lockup">
    <span class="brand-mark"></span>
    <span class="brand-name">Corvane<br>Property Group</span>
  </div>
  <p class="licence">Real Estate Lic: 5172093 &amp; 5172094</p>

  <div class="skyline-art" role="img" aria-label="Faint apartment building facade"></div>

  <div class="contact-block">
    <h1 class="person-name">DANIEL MARSH</h1>
    <p class="person-role">Director</p>
    <ul class="contact-list">
      <li>
        <svg class="contact-icon" viewBox="0 0 20 20" aria-hidden="true">
          <circle cx="10" cy="10" r="10" fill="#fff"/>
          <path d="M7 5.5 L8.6 5.3 L9.4 7.8 L8.4 8.7 C9 10 10 11 11.3 11.6 L12.2 10.6 L14.7 11.4 L14.5 13 C14.3 13.8 13.6 14.3 12.8 14.2 C9 13.6 6.4 11 5.8 7.2 C5.7 6.4 6.2 5.7 7 5.5 Z" fill="#5e5e5e"/>
        </svg>
        0400 318 726
      </li>
      <li>
        <svg class="contact-icon" viewBox="0 0 20 20" aria-hidden="true">
          <circle cx="10" cy="10" r="10" fill="#fff"/>
          <rect x="5" y="6.5" width="10" height="7" rx="1" fill="#5e5e5e"/>
          <path d="M5.5 7 L10 10.5 L14.5 7" fill="none" stroke="#fff" stroke-width="1"/>
        </svg>
        daniel@corvane.com.au
      </li>
      <li>
        <svg class="contact-icon" viewBox="0 0 20 20" aria-hidden="true">
          <circle cx="10" cy="10" r="10" fill="#fff"/>
          <g fill="none" stroke="#1f55b5" stroke-width="1">
            <circle cx="10" cy="10" r="5"/>
            <ellipse cx="10" cy="10" rx="2.2" ry="5"/>
            <line x1="5" y1="10" x2="15" y2="10"/>
          </g>
        </svg>
        www.corvane.com.au
      </li>
    </ul>
  </div>
</section>

<section class="card card-back">
  <div class="house-art" role="img" aria-label="Faint photo of a two-storey family home"></div>
  <h2 class="tagline">PROPERTY DEVELOPMENT<br>&amp; SITE ACQUISITION SPECIALISTS</h2>
  <div class="back-lockup">
    <span class="brand-mark"></span>
    <span class="brand-name">CORVANE<br>PROPERTY GROUP</span>
  </div>
  <p class="invite">Ask me about our INVESTMENT &amp; PARTNERSHIP opportunities</p>
</section>

</body>
</html>
```